Cat-products company needs smart, yet endearing, business card

We need a business card design for a new, but up-and-running, business based in Honolulu, Hawaii. The business is Purrlane Nest Co. Our first product is the most environmentally-friendly cat grass kit ever seen on the planet. Future products, currently in the R&D phase, will include a variety of exciting cat scratchers. We also do consulting work to help apartment-dwellers make their home more cat-friendly and, in the future, plan on doing full, custom installs of structure to create high walkways for cats.

Target Market(s)

Middle-aged, apartment-dwelling, middle-class workers who own 1 or more cats and who dote on them.

Industry/Entity Type

Pet Care

Contact Information for Business Card

A striking, professional, yet warm and friendly design is what we're after.

Font styles to use
Serif
Sans Serif
Other font styles liked:
• Comfortaa

Colors

Designer to choose colors to be used in the design.

Requirements
Must have
• The company logo: (see attachment)
• The company name: Purrlane Nest Co
• The web address: www.purrlanenestco.example
• Email: support@purrlanenestco.example
• Phone: +1 (808) 555 0172
• Update (Fri Jun 30 3017 7:45pm Hawaii Time) I would like, is possible, uploaded picture of the cat grass kit on the back of the card with some text along the lines of: Purrlane Nest Co - Where The Freshest Kitty Sprouts Begin
Nice to have
• A cat picture, cartoon, real or silhouette that illustrates cats in action and/or relaxing; ie using the apartment space to live, play and relax in and being well-contented.
• Most of the website is done in the font: Comfortaa. It might be nice to continue using this for brand consistency.
Should not have
• Hard-to-read fonts.

```html
<!DOCTYPE html>
<html lang="en">
<head>
<meta charset="utf-8">
<title>Purrlane Nest Co — Business Card</title>
<link rel="stylesheet" href="https://fonts.googleapis.com/css2?family=Comfortaa:wght@400;500;700&display=swap">
<style>
  :root {
    --stage: #000000;
    --paper: #f1e2c7;
    --ink: #4a2b22;
    --ink-soft: #8a6f63;
    --grass: #5daa3e;
    --sun: #f5b41a;
    --cat-tone: #b27a5c;
    --cat-light: #c99a79;
    --yarn: #d8262c;
  }
  * { margin: 0; padding: 0; box-sizing: border-box; }
  html, body {
    width: 1200px; height: 769px; overflow: hidden;
    background: var(--stage);
    font-family: "Comfortaa", sans-serif;
    color: var(--ink);
  }
  .canvas { position: relative; width: 1200px; height: 769px; }

  .card {
    position: absolute; left: 304px; width: 609px; height: 347px;
    background: var(--paper); overflow: hidden;
  }
  .card--front { top: 21px; }
  .card--back { top: 396px; height: 348px; }

  /* front */
  .holder-name { position: absolute; left: 37px; top: 50px; font-size: 32px; font-weight: 500; letter-spacing: 0.5px; white-space: nowrap; }
  .holder-role { position: absolute; left: 37px; top: 98px; font-size: 17px; color: var(--ink-soft); }
  .contact-list { position: absolute; left: 37px; top: 124px; list-style: none; }
  .contact-item { display: flex; align-items: center; height: 23px; margin-bottom: 14.5px; font-size: 18px; font-weight: 500; white-space: nowrap; }
  .contact-icon {
    width: 23px; height: 23px; border-radius: 3px; background: var(--ink);
    display: flex; align-items: center; justify-content: center; margin-right: 26px; flex: none;
  }
  .brand-mark { position: absolute; display: flex; align-items: center; gap: 8px; }
  .brand-mark--front { right: 26px; top: 62px; }
  .brand-dot { width: 18px; height: 18px; border-radius: 50%; background: var(--sun); flex: none; }
  .brand-name { font-weight: 700; color: var(--ink); line-height: 1.1; }
  .brand-mark--front .brand-name { font-size: 17px; width: 92px; }
  .grass-band {
    position: absolute; left: 0; top: 249px; width: 591px; height: 87px;
    background: var(--grass); border-radius: 0 10px 10px 0;
  }
  .cat-scene {
    position: absolute; left: 420px; top: 205px; width: 180px; height: 131px;
    border-radius: 50px 24px 24px 50px;
    background: linear-gradient(90deg, var(--cat-tone), var(--cat-light));
  }

  /* back */
  .grass-panel { position: absolute; inset: 0; }
  .kit-photo {
    position: absolute; left: 19px; top: 95px; width: 288px; height: 220px; border-radius: 6px;
    background: linear-gradient(135deg, #e7dcc3 0%, #d6c8a6 55%, #8fb870 100%);
  }
  .brand-mark--back { left: 400px; top: 62px; width: 150px; flex-direction: column; }
  .brand-mark--back .brand-name { font-size: 22px; text-align: center; width: 150px; }
  .company-name { position: absolute; left: 332px; width: 260px; top: 200px; text-align: center; font-size: 26px; font-weight: 500; white-space: nowrap; }
  .company-tagline { position: absolute; left: 342px; width: 240px; top: 251px; text-align: center; font-size: 18px; font-weight: 500; line-height: 26px; letter-spacing: 0.5px; white-space: nowrap; }
</style>
</head>
<body>
<main class="canvas">

  <section class="card card--front" aria-label="Business card front">
    <h1 class="holder-name">Kai Mahoe</h1>
    <p class="holder-role">Director</p>
    <ul class="contact-list">
      <li class="contact-item">
        <span class="contact-icon">
          <svg width="13" height="13" viewBox="0 0 24 24"><path fill="#f5b41a" d="M6.6 10.8a15 15 0 0 0 6.6 6.6l2.2-2.2c.3-.3.7-.4 1-.2 1.1.4 2.3.6 3.6.6.6 0 1 .4 1 1V20c0 .6-.4 1-1 1A17 17 0 0 1 3 4c0-.6.4-1 1-1h3.5c.6 0 1 .4 1 1 0 1.3.2 2.5.6 3.6.1.3 0 .7-.2 1z"/></svg>
        </span>+1 (808) 555 0172
      </li>
      <li class="contact-item">
        <span class="contact-icon">
          <svg width="13" height="13" viewBox="0 0 24 24"><circle cx="12" cy="12" r="10" fill="#f5b41a"/><path d="M2 12h20M12 2c3 3 3 17 0 20M12 2c-3 3-3 17 0 20" stroke="#4a2b22" stroke-width="1.6" fill="none"/></svg>
        </span>www.purrlanenestco.example
      </li>
      <li class="contact-item">
        <span class="contact-icon">
          <svg width="14" height="11" viewBox="0 0 24 18"><rect width="24" height="18" rx="2" fill="#f5b41a"/><path d="M1 2l11 8 11-8" stroke="#4a2b22" stroke-width="2" fill="none"/></svg>
        </span>support@purrlanenestco.example
      </li>
    </ul>
    <div class="brand-mark brand-mark--front">
      <span class="brand-dot"></span>
      <span class="brand-name">Purrlane Nest Co</span>
    </div>
    <div class="grass-band"></div>
    <div class="cat-scene" role="img" aria-label="Illustration of a contented cartoon cat lying on the grass playing with a red ball of yarn"></div>
  </section>

  <section class="card card--back" aria-label="Business card back">
    <svg class="grass-panel" width="609" height="348" viewBox="0 0 609 348" aria-hidden="true">
      <polygon points="388,0 609,0 609,348 284,348" fill="var(--grass)"/>
    </svg>
    <div class="kit-photo" role="img" aria-label="Photo of two cat grass kit boxes"></div>
    <div class="brand-mark brand-mark--back">
      <span class="brand-dot"></span>
      <span class="brand-name">Purrlane Nest Co</span>
    </div>
    <h2 class="company-name">Purrlane Nest Co</h2>
    <p class="company-tagline">Where The Freshest<br>Kitty Sprouts Begin</p>
  </section>

</main>
</body>
</html>
```